Wordpress Design For Financial Investment Company

//** NEW WIREFRAME ADDED TO HELP WITH LAYOUT ISSUES. PLEASE REFER TO WIREFRAME IN ATTACHED FILES. NO DESIGN WILL BE CONSIDERED IF IT DOES NOT FOLLOW THE WIREFRAME. **//
//** PLEASE READ THE ENTIRE BRIEF INCLUDING ALL UPDATES TO THE BRIEF. THE CLIENT IS VERY SPECIFIC ABOUT WHAT THEY WANT AND I'VE COVERED SEVERAL THINGS IN THE UPDATES. THERE IS ALSO A VIDEO UPDATE THAT HAS SOME VALUABLE INFORMATION IN IT FOR THIS CONTEST. **//
The client is an investment advisor who needs a new website designed. The current site is http://www.velmorfield.net.
The client wants the site to be green to match the attached logo.
The home page should have relevant images in the rotator. No people hugging! This is a financial investment site, not a family counseling site.
Also, the client wants 4 buttons on the home page to highlight the 4 main areas they focus on:
Investment Advice and Education
General Financial Planning
Retirement Planning
401K Planning
The top right area of the site needs to have their phone number, a call to action, and 2 buttons.
Their phone number is 303-418-7639
The call to action should say something like "Call for a free consultation!"
The buttons need to say:
Login To Your Bluvexa Account
Login To Your Quillbrook Account
The final design should communicate professionalism, financial safety and growth.
Main navigation should be:
Home
About Us
Associates
Services
Contact
Mission Statement (Could also be "Our Mission")
This is a site that the client likes: http://www.pwkinvestmentconsulting.com/
Updates
The designs should not have:
Newsletter content. A newsletter sign up is fine
Learning Center
Calculators
Stock prices/tickers
The design should have a contact form on the page.
I have talked to my client and have some updates. I did a video update because I thought it would be easier to show what I'm trying to get across.
Reason: I am going to be extending the contest a few more days. I'm still not getting quite what I want and very few people are even trying to follow the creative brief and the updates to it.
PLEASE read the entire brief and the updates. There is also a video I made that explains everything. I've also attached a wireframe.
Thanks!
Target Market(s)
People looking for a high-end financial investment company.
Industry/Entity Type
Investment
Requirements
Must have
- !!FOLLOW THE WIREFRAME FOR LAYOUT!!
!!THEIR LOGO!!
4 buttons to highlight their main practice areas
Phone number in the top right
"Free Consultation" call to action
2 Login buttons in the top right
A contact form on the page.
Should not have
- The designs should not have:
Learning Center
Calculators
Stock prices/tickers

```html
<!DOCTYPE html>
<html lang="en">
<head>
<meta charset="utf-8">
<title>Velmorfield Financial, Inc.</title>
<link rel="stylesheet" href="https://fonts.googleapis.com/css2?family=Lora:ital,wght@0,400;0,700;1,400&family=Open+Sans:wght@700&family=Playfair+Display:ital,wght@1,400;1,700&display=swap">
<style>
:root{
  --green:#2e8b4a;
  --green-dark:#1f6e36;
  --green-active:#1f5e12;
  --topbar:#2e2e2e;
  --red:#c0161a;
  --red-dark:#8e0d10;
  --yellow:#fbb316;
  --yellow-dark:#d98a06;
  --paper:#f4f4f2;
  --text-grey:#7a7a7a;
  --heading-green:#2d6e3c;
}
*{margin:0;padding:0;box-sizing:border-box}
html,body{width:1200px;height:1037px;overflow:hidden}
body{position:relative;background:var(--paper);font-family:"Lora",Georgia,serif;color:#333}
.abs{position:absolute}
.hero-photo{left:0;top:0;width:1200px;height:624px;background:radial-gradient(ellipse at 50% 45%,#6a6a6a 0%,#3e3e3e 55%,#262626 100%)}
.top-bar{left:0;top:0;width:1200px;height:49px;background:rgba(40,40,40,.85)}
.nav-band{left:0;top:49px;width:1200px;height:68px;background:linear-gradient(#35a053,var(--green));border-bottom:1px solid var(--green-dark)}
.btn{display:flex;align-items:center;justify-content:center;color:#fff;border-radius:3px}
.btn-red{background:linear-gradient(#d31d21,var(--red));box-shadow:0 4px 0 var(--red-dark)}
.btn-yellow{background:linear-gradient(#ffc732,var(--yellow));box-shadow:0 4px 0 var(--yellow-dark);color:#3a2300}
.top-btn{top:10px;height:29px;font-size:12px}
.top-phone{left:969px;top:13px;font-size:17px;color:#fff}
.brand{left:121px;top:19px;width:138px;height:138px;border-radius:50%;background:var(--green);display:flex;align-items:center;justify-content:center;text-align:center;color:#fff;font-size:15px;font-weight:700;line-height:1.3;box-shadow:0 3px 6px rgba(0,0,0,.3)}
.main-nav{top:49px;height:68px;display:flex;align-items:center;font-size:15px;color:#fff}
.main-nav a{color:#fff;text-decoration:none;position:absolute;top:0;height:68px;display:flex;align-items:center;justify-content:center}
.main-nav a.active{background:var(--green-active)}
.hero-title{left:0;width:1200px;top:226px;text-align:center;font-family:"Open Sans",Arial,sans-serif;font-weight:700;font-size:56px;color:#fff;letter-spacing:.5px}
.hero-sub{left:0;width:1200px;top:300px;text-align:center;font-family:"Playfair Display",Georgia,serif;font-style:italic;font-size:44px;color:#fff}
.hero-btn{top:410px;width:340px;height:54px;font-size:14px;letter-spacing:.3px}
.dot{top:509px;width:13px;height:13px;border-radius:50%;background:#eee}
.dot.on::after{content:"";position:absolute;left:4px;top:4px;width:5px;height:5px;border-radius:50%;background:var(--green)}
.panel{left:129px;top:550px;width:941px;height:331px;background:#fff;box-shadow:0 1px 3px rgba(0,0,0,.2)}
.contact-col{left:129px;top:550px;width:189px;height:331px;background:linear-gradient(#2f8d4a,var(--green-dark))}
.contact-tab{left:99px;top:624px;width:40px;height:197px;background:var(--green-dark);border-radius:3px 0 0 3px}
.contact-title{left:148px;top:564px;font-family:"Playfair Display",Georgia,serif;font-style:italic;font-size:29px;color:#123d1e}
.contact-line{left:147px;color:#fff;font-size:12px;line-height:17px}
.sep{left:129px;width:171px;height:1px;background:rgba(255,255,255,.2)}
.icon{left:110px}
.cta{left:139px;top:813px;width:169px;height:42px;font-size:12px}
.card{top:550px;width:189px;height:331px}
.card.shade{background:#f3f3f3}
.card-title{position:absolute;left:17px;top:26px;font-family:"Playfair Display",Georgia,serif;font-style:italic;font-size:13px;color:var(--heading-green);line-height:17px}
.card-img{position:absolute;left:17px;top:75px;width:151px;height:102px;background:linear-gradient(135deg,#bdbdbd,#555)}
.card-text{position:absolute;left:17px;top:193px;width:158px;font-style:italic;font-size:10.5px;line-height:13.8px;color:var(--text-grey)}
.learn{position:absolute;left:17px;top:290px;height:20px;width:82px;background:var(--red);color:#fff;font-style:italic;font-weight:700;font-size:10.5px;padding-left:12px;line-height:20px;clip-path:polygon(0 0,88% 0,100% 50%,88% 100%,0 100%)}
.vrule{top:576px;width:1px;height:262px;background:#e3e3e3}
.footer-rule{left:129px;top:938px;width:941px;height:1px;background:#ddd}
.footer-links{left:0;width:1200px;top:977px;text-align:center;font-style:italic;font-size:10px;color:#666}
.footer-links span{margin:0 5px;color:#aaa}
.copyright{left:0;width:1200px;top:997px;text-align:center;font-style:italic;font-size:10px;color:#666}
</style>
</head>
<body>
<div class="abs hero-photo" role="img" aria-label="Black and white group photo of the advisory team in business attire"></div>
<div class="abs top-bar"></div>
<div class="abs nav-band"></div>

<div class="abs btn btn-red top-btn" style="left:653px;width:99px">Join Us NOW</div>
<div class="abs btn btn-yellow top-btn" style="left:760px;width:168px">Call for a FREE Consultation!</div>
<svg class="abs" style="left:942px;top:15px" width="19" height="19" viewBox="0 0 20 20"><circle cx="10" cy="10" r="9.5" fill="#fff"/><path d="M6 5c1-1 2 0 2.5 1.5S8 8.5 8.3 9.3s1.4 2.3 2.4 2.4 1.5-.7 2.3-.2 1.8 1.6.8 2.5-3 .8-5-1.2S5 6 6 5z" fill="#333"/></svg>
<div class="abs top-phone">303-418-7639</div>

<div class="abs brand">Velmorfield<br>Financial, Inc.</div>

<nav class="abs main-nav" style="left:0;width:1200px">
  <a style="left:513px">Home</a>
  <a class="active" style="left:569px;width:95px">About Us</a>
  <a style="left:675px">Associates</a>
  <a style="left:773px">Services</a>
  <a style="left:857px">Contact</a>
  <a style="left:938px">Mission Statement</a>
</nav>

<div class="abs hero-title">“ALWAYS DO RIGHT.</div>
<div class="abs hero-sub">This will gratify some people &amp; astonish the rest.”</div>
<div class="abs btn btn-red hero-btn" style="left:254px">LOGIN TO YOUR BLUVEXA ACCOUNT</div>
<div class="abs btn btn-yellow hero-btn" style="left:608px">LOGIN TO YOUR BLUVEXA ACCOUNT</div>
<div class="abs dot" style="left:570px"></div>
<div class="abs dot on" style="left:586px"></div>
<div class="abs dot" style="left:602px"></div>
<div class="abs dot" style="left:619px"></div>

<div class="abs panel"></div>
<div class="abs contact-tab"></div>
<div class="abs contact-col"></div>
<div class="abs contact-title">Contact Us</div>
<svg class="abs icon" style="top:637px" width="12" height="14" viewBox="0 0 12 16"><path d="M6 0a5 5 0 0 1 5 5c0 4-5 10-5 10S1 9 1 5a5 5 0 0 1 5-5z" fill="#fff"/><circle cx="6" cy="5" r="2" fill="#1f6e36"/></svg>
<div class="abs contact-line" style="top:623px">Velmorfield Financial, Inc.<br>2840 Larkspur Avenue #210<br>Alderbrook, CO 80442</div>
<div class="abs sep" style="top:688px"></div>
<svg class="abs icon" style="top:703px" width="15" height="15" viewBox="0 0 20 20"><path d="M5 3c1.5-1.5 3 0 3.5 2S7.5 8 8 9s2 3 3 3.5 2.5-1.5 4-1 3 2 1.5 3.5-4 1.5-7-1.5S3.5 4.5 5 3z" fill="#fff"/></svg>
<div class="abs contact-line" style="top:701px;font-size:16px;line-height:20px">303-418-7639</div>
<div class="abs sep" style="top:736px"></div>
<svg class="abs icon" style="top:758px" width="15" height="11" viewBox="0 0 15 11"><rect width="15" height="11" fill="#fff"/><path d="M0 0l7.5 6L15 0" fill="none" stroke="#1f6e36" stroke-width="1.2"/></svg>
<div class="abs contact-line" style="top:755px">hello@velmorfield.net</div>
<div class="abs sep" style="top:788px"></div>
<div class="abs btn btn-yellow cta">Call for a FREE Consultation!</div>

<div class="abs card" style="left:318px">
  <div class="card-title">Investment Advice,<br>Education &amp; Calculators</div>
  <div class="card-img" role="img" aria-label="Businessman holding a calculator and receipt roll"></div>
  <div class="card-text">Lorem Ipsum is simply dummy text of the printing typesetting industry. Lorem Ipsum been the standard dummy text ever since the 1500s, when an... unknown</div>
  <div class="learn">Learn more</div>
</div>
<div class="abs vrule" style="left:506px"></div>
<div class="abs card" style="left:506px">
  <div class="card-title">General Financial<br>Planning</div>
  <div class="card-img" role="img" aria-label="Woman stacking coins on a table"></div>
  <div class="card-text">Lorem Ipsum is simply dummy text of the printing typesetting industry. Lorem Ipsum been the standard dummy text ever since the 1500s, when an... unknown</div>
  <div class="learn">Learn more</div>
</div>
<div class="abs card shade" style="left:692px">
  <div class="card-title">Retirement Planning</div>
  <div class="card-img" role="img" aria-label="Retired couple smiling with a laptop" style="background:linear-gradient(135deg,#e8e2da,#8fa3b8)"></div>
  <div class="card-text">Lorem Ipsum is simply dummy text of the printing typesetting industry. Lorem Ipsum been the standard dummy text ever since the 1500s, when an... unknown</div>
  <div class="learn">Learn more</div>
</div>
<div class="abs vrule" style="left:881px"></div>
<div class="abs card" style="left:881px">
  <div class="card-title">401K Planning</div>
  <div class="card-img" role="img" aria-label="Elderly couple sitting on a park bench"></div>
  <div class="card-text">Lorem Ipsum is simply dummy text of the printing typesetting industry. Lorem Ipsum been the standard dummy text ever since the 1500s, when an... unknown</div>
  <div class="learn">Learn more</div>
</div>

<div class="abs footer-rule"></div>
<div class="abs footer-links">Firm<span>|</span>Associates<span>|</span>Location<span>|</span>Services<span>|</span>Qualifications<span>|</span>Articles<span>|</span>External Page<span>|</span>Mission Statement<span>|</span>Core Values<span>|</span>Tell A Friend</div>
<div class="abs copyright">Copyright © 2013. Velmorfield Financial, Inc.</div>
</body>
</html>
```